STATIONERY FOR OUR CLIENT

I have a client that is a major oilseed processor in Australia. They want a deluxe gorgeous version of their business card.
I am proposing we print the business cards in Pelbrix.com VARNO versions with the coloured edging, probably in black. Their business name needs to appear on both sides whether in logo or text.
The stationery needs to be layed up to look lifelike to impress the client. Ideally full stationery including letterhead, business card, with compliments, envelopes.
We want to impress our client.
*** The design needs to communicate - quality, premium, prestige, modern, expert, wealthy, abundant, sophisticated, established.
Designs need to be not too dark, not alot of black please. Clean, modern, sophisticated, upmarket, luxury brand.
I need 3 concepts to present to client and once approved, refined to then have print ready files - and working files just in case we have to make tweaks down the track.
We also need to create a one page style guide, that includes pms colour etc.
THIS IS AN URGENT JOB
Updates

Please design less with black more with clean white possibly light grey/beige as secondary colour if you are looking for contrast. I have added some examples of cards that look nice and might help with what the client is looking for. thank you and looking forward to seeing the designs

Please ensure all designs submitted have the correct contact details of our client which is in the brief. Also please do not have any black backgrounds - if any of your design do have black backgrounds, please amend. Thank you

Target Market(s)

business customers, investors, major distributors

Industry/Entity Type

Business

Font styles to use
Sans Serif

Requirements
Must have
• must have business name on both sides. designed to be printed with pelbrix.com using their VARNO business card print offering.
Should not have
• alot of black

```html
<!DOCTYPE html>
<html lang="en">
<head>
<meta charset="utf-8">
<title>Kavella Oils &amp; BioEnergy – Business Card</title>
<link rel="stylesheet" href="https://fonts.googleapis.com/css2?family=Montserrat:wght@700&family=Questrial&display=swap">
<style>
  :root {
    --page-bg: #eeece7;
    --card-white: #ffffff;
    --card-tint: #e4f4f2;
    --teal-deep: #17a396;
    --teal-panel: #3db5a8;
    --brand-green: #118a4e;
    --text-light: #ffffff;
  }
  html, body {
    margin: 0;
    width: 1200px;
    height: 1200px;
    overflow: hidden;
    background: var(--page-bg);
  }
  .business-card {
    position: absolute;
    left: 80px;
    top: 282px;
    width: 1040px;
    height: 636px;
    box-shadow: 0 10px 30px rgba(0,0,0,0.18);
  }
  .business-card svg { display: block; }
  .brand-name {
    font-family: "Questrial", sans-serif;
    fill: var(--brand-green);
  }
  .holder-name {
    font-family: "Montserrat", sans-serif;
    font-weight: 700;
    fill: var(--text-light);
  }
  .holder-title, .contact-line {
    font-family: "Questrial", sans-serif;
    fill: var(--text-light);
  }
  .contact-icon { fill: var(--teal-deep); }
  .contact-icon-line {
    fill: none;
    stroke: var(--teal-deep);
    stroke-width: 3;
    stroke-linecap: round;
  }
</style>
</head>
<body>
<div class="business-card">
  <svg width="1040" height="636" viewBox="0 0 1040 636" xmlns="http://www.w3.org/2000/svg">
    <defs>
      <linearGradient id="cardTint" x1="0" y1="0" x2="1" y2="1">
        <stop offset="0" stop-color="#ffffff"/>
        <stop offset="1" stop-color="#e4f4f2"/>
      </linearGradient>
    </defs>

    <rect class="card-face" width="1040" height="636" fill="url(#cardTint)" role="img" aria-label="Fine diagonal pinstripe texture in pale teal across the card"/>

    <g class="name-badge">
      <circle cx="380" cy="506" r="131" fill="var(--card-white)"/>
      <circle cx="380" cy="506" r="128" fill="none" stroke="var(--teal-deep)" stroke-width="3"/>
      <circle cx="380" cy="506" r="119" fill="var(--teal-deep)"/>
      <text class="holder-name" x="380" y="494" font-size="29" text-anchor="middle">M.J. ORLAND</text>
      <text class="holder-title" x="380" y="526" font-size="21" text-anchor="middle">Managing Director</text>
    </g>

    <g class="brand-seal">
      <circle cx="251" cy="251" r="207" fill="var(--card-white)"/>
      <circle cx="251" cy="251" r="205" fill="none" stroke="var(--teal-deep)" stroke-width="3"/>
      <circle cx="251" cy="251" r="190" fill="var(--teal-deep)"/>
      <circle cx="251" cy="251" r="174" fill="var(--card-white)"/>
      <text class="brand-name" x="251" y="262" font-size="58" letter-spacing="10" text-anchor="middle">KAVELLA</text>
      <text class="brand-name" x="251" y="306" font-size="22" text-anchor="middle">Oils &amp; BioEnergy</text>
    </g>

    <rect class="contact-panel" x="568" y="108" width="423" height="448" rx="30" fill="var(--teal-panel)"/>

    <g class="contact-icons">
      <path class="contact-icon" d="M549 134 a11 11 0 0 1 11 11 c0 9 -11 22 -11 22 c0 0 -11 -13 -11 -22 a11 11 0 0 1 11 -11z M549 140 a5 5 0 1 0 0.01 0z" fill-rule="evenodd"/>
      <path class="contact-icon" d="M540 262 l6 -3 l5 9 l-4 3 c2 5 6 9 11 11 l3 -4 l9 5 l-3 6 c-14 2 -29 -13 -27 -27z"/>
      <path class="contact-icon" d="M543 306 h13 a2 2 0 0 1 2 2 v24 a2 2 0 0 1 -2 2 h-13 a2 2 0 0 1 -2 -2 v-24 a2 2 0 0 1 2 -2z M545 310 v18 h9 v-18z" fill-rule="evenodd"/>
      <path class="contact-icon" d="M539 411 h22 v15 h-22z M540 412 l10 8 l10 -8" stroke="var(--card-white)" stroke-width="1.5"/>
      <circle class="contact-icon" cx="550" cy="455" r="11"/>
      <path d="M539 455 h22 M550 444 v22 M550 444 c-7 6 -7 16 0 22 M550 444 c7 6 7 16 0 22" stroke="var(--card-white)" stroke-width="1.5" fill="none"/>
      <g class="link-icon">
        <rect class="contact-icon-line" x="538" y="493" width="14" height="9" rx="4.5" transform="rotate(-45 545 497.5)"/>
        <rect class="contact-icon-line" x="548" y="493" width="14" height="9" rx="4.5" transform="rotate(-45 555 497.5)"/>
      </g>
    </g>

    <g class="contact-details">
      <text class="contact-line" x="581" y="159" font-size="28">Unit 5, 48 Ferncliff Road</text>
      <text class="contact-line" x="581" y="204" font-size="28">Marlow VIC 3199</text>
      <text class="contact-line" x="583" y="292" font-size="28">03 5550 1427</text>
      <text class="contact-line" x="583" y="335" font-size="28">0491 570 318</text>
      <text class="contact-line" x="585" y="427" font-size="28">kavellaoil@mailbox.net</text>
      <text class="contact-line" x="585" y="470" font-size="28">kavellaoils.com.au</text>
      <text class="contact-line" x="585" y="511" font-size="28">connect.kavellaoils.com.au</text>
    </g>
  </svg>
</div>
</body>
</html>
```